Tabletop Sign for Support Coordination Service

We need a design for a table top sign for a Support Coordination enterprise. We find and coordinate support services for those with various disabilities. We would like designs that incorporate our logo and colors, blues and greens as seen in the file upload. Additionally, we would also preferably like designs with a more modern feel. The final design should include all these in addition to our contact information (email and telephone).

```html
<!DOCTYPE html>
<html lang="en">
<head>
<meta charset="utf-8">
<title>Lumen Support Services – Tabletop Sign</title>
<link href="https://fonts.googleapis.com/css2?family=Oswald:wght@400;500;600&family=Montserrat:wght@700&display=swap" rel="stylesheet">
<style>
  :root{
    --stage:#33404f;
    --navy:#2a4b74;
    --navy-dark:#1f3d66;
    --green:#6abd45;
    --white:#ffffff;
    --paper:#f6f6f6;
    --photo-a:#8a8f8c;
    --photo-b:#6f7c5a;
    --photo-c:#4a4f45;
  }
  *{margin:0;padding:0;box-sizing:border-box}
  html,body{width:1200px;height:1200px;overflow:hidden;background:var(--stage)}
  .stage{position:relative;width:1200px;height:1200px}
  .sign{position:absolute;top:230px;width:423px;height:739px;overflow:hidden;background:var(--green)}
  .sign--left{left:137px}
  .sign--right{left:639px}
  .sign__art{position:absolute;inset:0;width:423px;height:739px}
  .brand{position:absolute;left:234px;width:160px;text-align:center}
  .brand__dot{position:absolute;left:287px;top:62px;width:54px;height:54px;border-radius:50%;background:var(--navy-dark)}
  .brand__name{top:128px;font-family:"Montserrat",sans-serif;font-weight:700;font-size:46px;line-height:60px;color:var(--green);letter-spacing:1px}
  .title{position:absolute;left:42px;top:212px;font-family:"Oswald",sans-serif;font-weight:500;font-size:50px;line-height:54px;color:var(--white)}
  .tagline{position:absolute;left:0;width:423px;text-align:center;font-family:"Oswald",sans-serif;font-weight:500;font-size:33px;line-height:40px}
  .tagline--service{top:436px;color:var(--green)}
  .tagline--motto{top:482px;color:var(--white)}
  .contact__phone{position:absolute;left:0;width:423px;top:578px;display:flex;justify-content:center;align-items:center;gap:18px;font-family:"Oswald",sans-serif;font-weight:500;font-size:50px;line-height:62px;color:var(--navy)}
  .contact__phone svg{width:40px;height:40px}
  .contact__rule{position:absolute;left:50px;top:651px;width:324px;height:3px;background:var(--navy)}
  .contact__web{position:absolute;left:0;width:423px;top:668px;text-align:center;font-family:"Oswald",sans-serif;font-weight:500;font-size:26px;line-height:36px;color:var(--navy)}
</style>
</head>
<body>
<div class="stage">

  <div class="sign sign--left">
    <svg class="sign__art" viewBox="0 0 529 923" preserveAspectRatio="none">
      <defs>
        <linearGradient id="photoTones" x1="0" y1="0" x2="0.6" y2="1">
          <stop offset="0" stop-color="#b9bcbb"/>
          <stop offset="0.45" stop-color="#7b7568"/>
          <stop offset="1" stop-color="#5f6b4a"/>
        </linearGradient>
      </defs>
      <rect x="0" y="0" width="529" height="620" fill="url(#photoTones)" role="img" aria-label="Photo of two smiling women hugging outdoors, one seated in a wheelchair"/>
      <circle cx="540" cy="-10" r="365" fill="var(--green)"/>
      <circle cx="540" cy="-10" r="350" fill="var(--paper)"/>
      <path d="M0 547 C140 480 300 450 529 440 L529 923 L0 923 Z" fill="var(--green)"/>
      <path d="M0 592 C140 510 300 470 529 455 L529 690 L0 690 Z" fill="var(--navy)"/>
    </svg>
    <span class="brand__dot"></span>
    <div class="brand brand__name">LUMEN</div>
    <h1 class="title">Lumen<br>Support<br>Services</h1>
    <p class="tagline tagline--service">Support Cordination</p>
    <p class="tagline tagline--motto">Navigation Abilities Together</p>
    <div class="contact__phone">
      <svg viewBox="0 0 24 24" fill="none" stroke="currentColor" stroke-width="1.8" stroke-linecap="round" stroke-linejoin="round" aria-hidden="true"><path d="M22 16.9v3a2 2 0 0 1-2.2 2 19.8 19.8 0 0 1-8.6-3.1 19.5 19.5 0 0 1-6-6A19.8 19.8 0 0 1 2.1 4.2 2 2 0 0 1 4.1 2h3a2 2 0 0 1 2 1.7c.1.9.4 1.8.7 2.7a2 2 0 0 1-.5 2.1L8 9.8a16 16 0 0 0 6 6l1.3-1.3a2 2 0 0 1 2.1-.5c.9.3 1.8.6 2.7.7a2 2 0 0 1 1.7 2z"/><path d="M15 5a5 5 0 0 1 4 4M15 1a9 9 0 0 1 8 8"/></svg>
      <span>(555) 214.0386</span>
    </div>
    <div class="contact__rule"></div>
    <p class="contact__web">WWW.LUMENSUPPORTSERVICES.COM</p>
  </div>

  <div class="sign sign--right">
    <svg class="sign__art" viewBox="0 0 529 923" preserveAspectRatio="none">
      <rect x="0" y="0" width="529" height="620" fill="url(#photoTones)" role="img" aria-label="Photo of two smiling women hugging outdoors, one seated in a wheelchair"/>
      <circle cx="540" cy="-10" r="365" fill="var(--green)"/>
      <circle cx="540" cy="-10" r="350" fill="var(--paper)"/>
      <path d="M0 547 C140 480 300 450 529 440 L529 923 L0 923 Z" fill="var(--green)"/>
      <path d="M0 592 C140 510 300 470 529 455 L529 690 L0 690 Z" fill="var(--navy)"/>
    </svg>
    <span class="brand__dot"></span>
    <div class="brand brand__name">LUMEN</div>
    <h2 class="title">Lumen<br>Support<br>Services</h2>
    <p class="tagline tagline--service">Support Cordination</p>
    <p class="tagline tagline--motto">Navigation Abilities Together</p>
    <div class="contact__phone">
      <svg viewBox="0 0 24 24" fill="none" stroke="currentColor" stroke-width="1.8" stroke-linecap="round" stroke-linejoin="round" aria-hidden="true"><path d="M22 16.9v3a2 2 0 0 1-2.2 2 19.8 19.8 0 0 1-8.6-3.1 19.5 19.5 0 0 1-6-6A19.8 19.8 0 0 1 2.1 4.2 2 2 0 0 1 4.1 2h3a2 2 0 0 1 2 1.7c.1.9.4 1.8.7 2.7a2 2 0 0 1-.5 2.1L8 9.8a16 16 0 0 0 6 6l1.3-1.3a2 2 0 0 1 2.1-.5c.9.3 1.8.6 2.7.7a2 2 0 0 1 1.7 2z"/><path d="M15 5a5 5 0 0 1 4 4M15 1a9 9 0 0 1 8 8"/></svg>
      <span>(555) 214.0386</span>
    </div>
    <div class="contact__rule"></div>
    <p class="contact__web">WWW.LUMENSUPPORTSERVICES.COM</p>
  </div>

</div>
</body>
</html>
```